Consulting firm needs a professional letterhead design

We need a professional letterhead design which is simple but unique. It should carry attributes of the latest designs in the market suitable for professional environmental consultancies.

- The logo is attached for you to USE.
- Our preferred color scheme is that shown in the logo.
- Letterhead text color is your choice to make.
- Logo to the left and text to the right plus slogan/tagline is desirable for this letterhead.

Use any address etc. of your choice in the letterhead.

Target Market(s)

Consulting firms and government agencies

Industry/Entity Type

Environmental Consultant

Colors
acd037
fece3e
85cae6
3277b5

Requirements
Must have
• Logo supplied and color scheme must be used.
Nice to have
• Nexa font is used in the Logo, so it would ne nice to have nexa font in the letterhead too.

```html
<!DOCTYPE html>
<html lang="en">
<head>
<meta charset="utf-8">
<title>Verdalys Letterhead</title>
<link rel="stylesheet" href="https://fonts.googleapis.com/css2?family=Montserrat:wght@500&family=Arimo&family=Lexend:wght@600&display=swap">
<style>
  :root {
    --brand-blue: #007bb0;
    --wave-grey: #a9aaad;
    --paper: #ffffff;
    --ink: #333338;
    --accent-green: #4cb944;
    --rule-blue: #1a8cc0;
  }
  html, body {
    margin: 0;
    padding: 0;
    overflow: hidden;
    background: var(--paper);
  }
  .letterhead {
    position: relative;
    width: 848px;
    height: 1200px;
    background: var(--paper);
    overflow: hidden;
  }
  .header-waves {
    position: absolute;
    top: 0;
    left: 0;
    width: 848px;
    height: 240px;
  }
  .brand {
    position: absolute;
    left: 85px;
    top: 38px;
    width: 168px;
    text-align: center;
    color: var(--paper);
    font-family: "Montserrat", sans-serif;
    font-weight: 500;
  }
  .brand-mark {
    display: block;
    width: 66px;
    height: 66px;
    margin: 0 auto 12px;
    border-radius: 50%;
    background: var(--accent-green);
  }
  .brand-name {
    display: block;
    font-size: 20px;
    letter-spacing: 2.6px;
    line-height: 1;
  }
  .brand-tagline {
    display: block;
    margin-top: 2px;
    font-size: 8.6px;
    line-height: 1.1;
    letter-spacing: 0.1px;
    white-space: nowrap;
  }
  .contact-list {
    position: absolute;
    left: 603px;
    top: 80px;
    margin: 0;
    padding: 0;
    list-style: none;
    font-family: "Arimo", sans-serif;
    font-size: 12.6px;
    color: var(--ink);
  }
  .contact-list li {
    display: flex;
    align-items: center;
    height: 24.6px;
  }
  .contact-icon {
    width: 14px;
    height: 14px;
    margin-right: 5px;
    color: var(--ink);
    flex: none;
  }
  .contact-at {
    margin-right: 5px;
  }
  .footer-rule {
    position: absolute;
    left: 0;
    top: 1142px;
    width: 848px;
    height: 4px;
    background: linear-gradient(to right, rgba(26,140,192,0) 0%, rgba(26,140,192,0.5) 25%, var(--rule-blue) 50%, rgba(26,140,192,0.5) 75%, rgba(26,140,192,0) 100%);
  }
  .footer-address {
    position: absolute;
    left: 0;
    top: 1153px;
    width: 848px;
    display: flex;
    justify-content: center;
    align-items: center;
    font-family: "Lexend", sans-serif;
    font-weight: 600;
    font-size: 11.6px;
    color: var(--ink);
  }
  .pin-icon {
    width: 18px;
    height: 26px;
    margin-right: 6px;
  }
</style>
</head>
<body>
<div class="letterhead">
  <svg class="header-waves" viewBox="0 0 848 240" aria-hidden="true">
    <path fill="var(--wave-grey)" d="M0 141 C50 205 100 227 155 227 C260 228 380 160 470 112 C560 65 630 38 680 28 C600 38 500 70 420 100 C320 140 230 200 155 200 C90 200 40 165 0 115 Z"/>
    <path fill="var(--brand-blue)" d="M0 0 H848 V24 C780 20 720 20 680 24 C580 32 480 70 400 105 C300 148 220 187 155 187 C90 187 40 150 0 110 Z"/>
  </svg>

  <div class="brand">
    <span class="brand-mark"></span>
    <span class="brand-name">VERDALYS</span>
    <span class="brand-tagline">Turning field data into sound policy</span>
  </div>

  <ul class="contact-list">
    <li>
      <svg class="contact-icon" viewBox="0 0 24 24"><path fill="currentColor" d="M6.6 2.5l3 4.2-2 1.8c.9 2.7 3 5.6 5.6 7.4l2.1-1.6 4 3.2-2.1 3.4C10 20 4 13 4 4.2z"/></svg>
      <span>: +91 500 1234 567</span>
    </li>
    <li>
      <span class="contact-at">@</span>
      <span>: office@verdalys.com</span>
    </li>
    <li>
      <svg class="contact-icon" viewBox="0 0 24 24" fill="none" stroke="currentColor" stroke-width="1.8"><circle cx="12" cy="12" r="10"/><ellipse cx="12" cy="12" rx="4.5" ry="10"/><path d="M2 12h20M3.5 7h17M3.5 17h17"/></svg>
      <span>: http://www.verdalysfirm.com</span>
    </li>
  </ul>

  <div class="footer-rule"></div>
  <div class="footer-address">
    <svg class="pin-icon" viewBox="0 0 18 26"><path fill="var(--ink)" d="M9 1a7.5 7.5 0 0 0-7.5 7.5C1.5 14 9 21 9 21s7.5-7 7.5-12.5A7.5 7.5 0 0 0 9 1zm0 10.2a2.8 2.8 0 1 1 0-5.6 2.8 2.8 0 0 1 0 5.6z"/><ellipse cx="9" cy="23" rx="7" ry="2.2" fill="none" stroke="var(--ink)" stroke-width="1.4"/></svg>
    <span>Plot No.118, Sunder Nagar, Lake View Road, Nashik.422001</span>
  </div>
</div>
</body>
</html>
```